Ridgeline Build Network Inc. Letterhead

Creation of attractive and eye catching letterhead for a business start-up for the construction industry. Letterhead must relate to construction, but avoid standard hammer and tools in the design.
Updates

I forgot to add some details, sorry about that. Some pertinent info: Ph: 916-555-0148 ridgelinebuildnet.example 487 Willowmere Ave, Ste 210 Folsom, CA 95699 info@ridgelinebuildnet.example not sure if slogan should be in there" “Connecting construction professionals to create a purpose driven industry.” must be able to be used in word. Thanks!

```html
<!DOCTYPE html>
<html lang="en">
<head>
<meta charset="utf-8">
<title>Ridgeline Build Network Inc. Letterhead</title>
<link rel="stylesheet" href="https://fonts.googleapis.com/css2?family=Montserrat:wght@600&family=Roboto+Condensed:wght@400;700&display=swap">
<style>
  :root {
    --backdrop: #bcbcbc;
    --paper: #ffffff;
    --navy: #222257;
    --red: #c1272d;
    --ink: #2a2a2a;
    --muted: #555555;
  }
  html, body {
    margin: 0;
    padding: 0;
    width: 1200px;
    height: 780px;
    overflow: hidden;
    background: var(--backdrop);
  }
  .letterhead {
    position: absolute;
    left: 330px;
    top: 40px;
    width: 540px;
    height: 700px;
    background: var(--paper);
    box-shadow: 0 4px 14px rgba(0,0,0,0.18);
    overflow: hidden;
  }
  .brand {
    position: absolute;
    left: 70px;
    top: 44px;
    display: flex;
    align-items: center;
    gap: 7px;
  }
  .brand-mark {
    width: 9px;
    height: 9px;
    background: var(--red);
  }
  .brand-name {
    font-family: "Montserrat", sans-serif;
    font-weight: 600;
    font-size: 10.5px;
    letter-spacing: 0.08em;
    color: var(--navy);
    text-transform: uppercase;
  }
  .corner-bands {
    position: absolute;
    left: 0;
    top: 0;
    width: 540px;
    height: 700px;
  }
  .band-red { fill: var(--red); }
  .band-navy { fill: var(--navy); }
  .contact {
    position: absolute;
    left: 66px;
    top: 584px;
    font-family: "Roboto Condensed", sans-serif;
    color: var(--muted);
    font-size: 6.5px;
    line-height: 9px;
    letter-spacing: 0.04em;
    text-transform: uppercase;
  }
  .contact-name {
    font-weight: 700;
    font-size: 9px;
    line-height: 12px;
    color: var(--ink);
  }
  .contact p { margin: 0; }
</style>
</head>
<body>
  <main class="letterhead">
    <header class="brand">
      <span class="brand-mark"></span>
      <span class="brand-name">Ridgeline Build Network</span>
    </header>

    <svg class="corner-bands" viewBox="0 0 540 700" aria-hidden="true">
      <polygon class="band-red" points="0,700 321,700 421,664"/>
      <polygon class="band-navy" points="321,700 540,700 540,620"/>
    </svg>

    <footer class="contact">
      <p class="contact-name">Ridgeline Build Network</p>
      <p>487 Willowmere Ave, Ste 210, Folsom CA</p>
      <p>Tel 916-555-0148</p>
      <p>info@ridgelinebuildnet.example ridgelinebuildnet.example</p>
    </footer>
  </main>
</body>
</html>
```